truck and trailer business Wrap Design

needing a redisgn of our truck and trailer wraps, i have attached the current trailer wrap design and pictures of the new trailer needing a wrap design. trailer is 26ft v nose. 8.5 wide and 7.5ft tall need the trucks that pull the trailers to match. 2018 r-380 long bed. i have attached pictures of the truck. 2009 ZOBI 26 FT BOX
Updates

Low design quality

Industry/Entity Type

Insulation

Colors

Designer to choose colors to be used in the design.

Requirements
Must have
• wrap needs to be unique and stand out like our current wrap

```html
<!DOCTYPE html>
<html lang="en">
<head>
<meta charset="utf-8">
<title>Summit Spray Foam — Trailer &amp; Truck Wrap</title>
<link href="https://fonts.googleapis.com/css2?family=Barlow+Condensed:wght@500;600;700&family=Montserrat:wght@600;700;800&display=swap" rel="stylesheet">
<style>
  :root{
    --board-light:#cfd0d2;
    --board-dark:#3c3c3e;
    --wrap-black:#0b0b0c;
    --wrap-charcoal:#2b2d30;
    --ink-white:#ffffff;
    --accent-blue:#2a9be0;
    --rule:#e8e8e8;
  }
  *{box-sizing:border-box;margin:0;padding:0}
  html,body{width:1200px;height:566px;overflow:hidden}
  body{
    position:relative;
    background:linear-gradient(to bottom,var(--board-light) 0 432px,var(--board-dark) 432px 100%);
    font-family:"Barlow Condensed",sans-serif;
    color:var(--ink-white);
  }
  .wrap-panel{
    position:absolute;
    background:linear-gradient(to bottom,var(--wrap-black) 0%,var(--wrap-black) 55%,var(--wrap-charcoal) 100%);
    box-shadow:3px 4px 6px rgba(0,0,0,.45);
    overflow:hidden;
  }
  .trailer-side{left:32px;width:830px;height:238px}
  .trailer-side.upper{top:32px}
  .trailer-side.lower{top:294px}
  .trailer-rear{left:896px;top:162px;width:272px;height:239px}

  .photo-strip{position:absolute;top:10px;width:320px;height:220px}
  .upper .photo-strip{left:502px}
  .lower .photo-strip{left:10px}

  .copy-block{position:absolute;top:0;width:440px}
  .upper .copy-block{left:50px}
  .lower .copy-block{left:339px}

  .service-list{
    font-weight:500;font-size:25px;letter-spacing:.3px;
    margin-top:28px;white-space:nowrap;line-height:1;
  }
  .rule{height:2px;background:var(--rule);margin:10px 0}
  .brand-name{
    font-family:"Montserrat",sans-serif;font-weight:800;
    color:var(--accent-blue);text-align:center;
    font-size:34px;line-height:34px;letter-spacing:2px;
  }
  .contact-line{
    font-weight:600;font-size:25px;color:var(--accent-blue);
    white-space:nowrap;margin-top:4px;line-height:1;
  }
  .social-row{
    display:flex;align-items:center;gap:8px;margin-top:14px;margin-left:4px;
    font-family:"Montserrat",sans-serif;font-weight:700;font-size:10.5px;white-space:nowrap;
  }
  .social-dot{width:22px;height:22px;border-radius:50%;background:var(--ink-white);flex:none}

  .rear-copy{position:absolute;inset:0;text-align:center;font-family:"Montserrat",sans-serif}
  .rear-tagline{font-weight:700;font-size:13px;line-height:16px;margin-top:46px}
  .rear-copy .rule{width:188px;margin:8px auto;height:1.5px}
  .rear-copy .brand-name{font-size:17px;line-height:20px;letter-spacing:1px}
  .rear-web{font-weight:600;font-size:9px;margin-top:50px}
  .rear-phone{font-weight:700;font-size:18px;line-height:20px}
  .rear-social{display:flex;justify-content:center;align-items:center;gap:6px;font-weight:700;font-size:8px;margin-top:4px}
  .rear-social .social-dot{width:15px;height:15px}
  .rear-band{position:absolute;left:0;right:0;bottom:0;height:6px;background:var(--ink-white)}
</style>
</head>
<body>

<section class="wrap-panel trailer-side upper">
  <div class="copy-block">
    <p class="service-list">SPRAY FOAM • FIBERGLASS • &nbsp;INSULATION • ROOFING</p>
    <div class="rule"></div>
    <p class="brand-name">SUMMIT<br>SPRAY FOAM</p>
    <div class="rule"></div>
    <p class="contact-line">SUMMITSPRAYFOAM.NET | 555-010-4821</p>
    <div class="social-row"><span class="social-dot"></span>SUMMITSPRAYFOAM | <em>DFW PREMIER INSULATION COMPANY</em></div>
  </div>
  <svg class="photo-strip" viewBox="0 0 320 220" role="img" aria-label="Three slanted photos of installers applying spray foam insulation in attic framing">
    <defs>
      <linearGradient id="photoWarm" x1="0" y1="0" x2="1" y2="1"><stop offset="0" stop-color="#e9ddc4"/><stop offset="1" stop-color="#b88a52"/></linearGradient>
      <linearGradient id="photoWood" x1="0" y1="0" x2="0" y2="1"><stop offset="0" stop-color="#c89a5c"/><stop offset="1" stop-color="#e2c48c"/></linearGradient>
      <linearGradient id="photoSuit" x1="0" y1="0" x2="1" y2="1"><stop offset="0" stop-color="#f2f2f0"/><stop offset="1" stop-color="#b9bcc2"/></linearGradient>
    </defs>
    <polygon points="40,0 140,0 100,220 0,220" fill="url(#photoWarm)"/>
    <polygon points="146,0 206,0 186,220 106,220" fill="url(#photoWood)"/>
    <polygon points="212,0 320,0 320,220 192,220" fill="url(#photoSuit)"/>
  </svg>
</section>

<section class="wrap-panel trailer-side lower">
  <svg class="photo-strip" viewBox="0 0 320 220" role="img" aria-label="Three slanted photos of installers applying spray foam insulation in attic framing">
    <polygon points="0,0 108,0 128,220 0,220" fill="url(#photoSuit)"/>
    <polygon points="114,0 174,0 214,220 134,220" fill="url(#photoWood)"/>
    <polygon points="180,0 280,0 320,220 220,220" fill="url(#photoWarm)"/>
  </svg>
  <div class="copy-block">
    <p class="service-list">SPRAY FOAM • FIBERGLASS • &nbsp;INSULATION • ROOFING</p>
    <div class="rule"></div>
    <p class="brand-name">SUMMIT<br>SPRAY FOAM</p>
    <div class="rule"></div>
    <p class="contact-line">SUMMITSPRAYFOAM.NET | 555-010-4821</p>
    <div class="social-row"><span class="social-dot"></span>SUMMITSPRAYFOAM | <em>DFW PREMIER INSULATION COMPANY</em></div>
  </div>
</section>

<section class="wrap-panel trailer-rear">
  <div class="rear-copy">
    <p class="rear-tagline">DFW PREMIER<br>INSULATION COMPANY</p>
    <div class="rule"></div>
    <p class="brand-name">SUMMIT SPRAY FOAM</p>
    <div class="rule"></div>
    <p class="rear-web">SUMMITSPRAYFOAM.NET</p>
    <p class="rear-phone">555-010-4821</p>
    <div class="rear-social"><span class="social-dot"></span>SUMMITSPRAYFOAM</div>
  </div>
  <div class="rear-band"></div>
</section>

</body>
</html>
```